Fleet Service Tri Fold Flyer

I am looking to come up with a flyer design to hand out showing our services. I will upload more info with working, but in the mean time want to just have a flyer to pass out. I have uploaded our logo and the images for it. I also uploaded what our trucks look like for ideas, as well as a business card.

Industry/Entity Type

Mobile Hydraulics and Fleet Service

Colors
0054AA
0677BA
7BADD7
CADEEF
E8F1F8
F0912C
F2A743
F7CA91
FBE8D2
FDF5EE

Requirements
Must have
• I uploaded a PDF with wording for the flyer

```html
<!DOCTYPE html>
<html lang="en">
<head>
<meta charset="utf-8">
<title>Ironline Fleet Services – Tri-Fold Brochure</title>
<link rel="stylesheet" href="https://fonts.googleapis.com/css2?family=Oswald:wght@400;500;600;700&family=Open+Sans:wght@400;600;700&display=swap">
<style>
  :root{
    --blue-deep:#0054AA;
    --blue:#0677BA;
    --blue-mid:#7BADD7;
    --blue-light:#CADEEF;
    --blue-pale:#E8F1F8;
    --orange:#F0912C;
    --gold:#F2A743;
    --peach:#F7CA91;
    --cream:#FBE8D2;
    --ivory:#FDF5EE;
    --ink:#1f2d3d;
    --stage:#e9e6e1;
    --white:#ffffff;
  }
  *{box-sizing:border-box;margin:0;padding:0}
  html,body{width:1200px;height:2398px;overflow:hidden}
  body{background:var(--stage);font-family:"Open Sans",Arial,sans-serif;color:var(--ink);position:relative}

  .sheet{position:absolute;left:30px;width:1140px;height:1040px;display:flex;box-shadow:0 6px 24px rgba(0,0,0,.18)}
  .sheet--outside{top:100px}
  .sheet--inside{top:1258px}
  .panel{position:relative;width:380px;height:1040px;overflow:hidden;background:var(--white)}
  .panel--blue{background:linear-gradient(180deg,var(--blue) 0%,var(--blue-deep) 100%);color:var(--white)}

  .photo{position:absolute;left:0;width:100%}
  .heading{font-family:"Oswald",Arial,sans-serif;font-weight:600;text-transform:uppercase;letter-spacing:.5px}

  /* brand name block */
  .brand{display:flex;align-items:center;gap:10px;justify-content:center}
  .brand__mark{width:22px;height:22px;background:var(--orange)}
  .brand__name{font-family:"Oswald",Arial,sans-serif;font-weight:700;font-size:34px;letter-spacing:1px;color:var(--blue-deep);text-transform:uppercase;line-height:1}
  .panel--blue .brand__name{color:var(--white)}

  /* 24 hours badge */
  .hours{display:flex;align-items:center;gap:6px}
  .hours__num{font-family:"Oswald",Arial,sans-serif;font-weight:700;font-size:40px;color:var(--orange);line-height:.9}
  .hours__label{font-family:"Oswald",Arial,sans-serif;font-weight:600;font-size:13px;color:var(--orange);letter-spacing:1px}

  /* call bar */
  .callbar{position:absolute;left:0;bottom:34px;width:100%;height:56px;background:var(--blue-deep);clip-path:polygon(0 30%,100% 0,100% 100%,0 100%);display:flex;align-items:flex-end;padding:0 22px 10px;gap:12px;color:var(--white);font-family:"Oswald",Arial,sans-serif}
  .callbar__label{font-size:17px;font-weight:500;color:var(--gold)}
  .callbar__phone{font-size:22px;font-weight:600;color:var(--gold);display:flex;align-items:center;gap:8px}

  /* cover */
  .cover__brand{position:absolute;top:70px;left:0;width:100%}
  .cover__photo{top:190px;height:520px;background:linear-gradient(180deg,var(--blue-mid) 0%,var(--blue-light) 35%,var(--peach) 62%,#b49466 100%);clip-path:polygon(0 0,100% 0,100% 82%,0 100%)}
  .cover__hours{position:absolute;top:740px;right:30px}
  .cover__title{position:absolute;top:820px;left:0;width:100%;text-align:center;font-size:44px;color:var(--blue-deep);font-weight:700}

  /* services panel */
  .services__photo{top:0;height:300px;background:linear-gradient(160deg,#8fb66c 0%,var(--blue-light) 45%,#f4f4f4 70%,#7d8a94 100%);clip-path:polygon(0 0,100% 0,100% 82%,0 100%)}
  .services__head{position:absolute;top:330px;left:32px;right:32px;display:flex;justify-content:space-between;align-items:center}
  .services__head h2{font-size:28px;color:var(--blue-deep)}
  .services__list{position:absolute;top:400px;left:32px;right:28px;list-style:none}
  .services__list li{position:relative;padding-left:26px;margin-bottom:12px;font-size:15px;line-height:1.35;color:var(--blue-deep)}
  .services__list li::before{content:"";position:absolute;left:2px;top:5px;width:10px;height:10px;border-radius:50%;background:var(--orange)}
  .services__tag{position:absolute;top:720px;left:32px;font-size:24px;color:var(--blue-deep)}
  .services__copy{position:absolute;top:765px;left:32px;right:28px;font-size:13px;line-height:1.55;color:#445}

  /* contact panel */
  .contact__brand{position:absolute;top:110px;left:0;width:100%}
  .contact__dot{position:absolute;top:160px;width:100%;text-align:center;font-size:13px;letter-spacing:1px;color:var(--blue-light)}
  .contact__lead{position:absolute;top:230px;width:100%;text-align:center;font-size:24px}
  .contact__title{position:absolute;top:270px;width:100%;text-align:center;font-size:34px;color:var(--gold);font-weight:700}
  .contact__bar{position:absolute;top:340px;left:30px;right:30px;height:44px;background:var(--gold);display:flex;align-items:center;justify-content:center;gap:12px;font-family:"Oswald",Arial,sans-serif;color:var(--blue-deep);font-weight:600;font-size:19px}
  .contact__lines{position:absolute;top:410px;left:46px;right:30px;font-size:16px;line-height:1.7;font-style:normal}
  .contact__photo{bottom:0;height:330px;background:linear-gradient(180deg,var(--blue-light) 0%,var(--gold) 55%,#6e6250 100%);clip-path:polygon(0 22%,100% 0,100% 100%,0 100%)}

  /* inside panels */
  .copy{position:absolute;left:34px;right:30px;font-size:14.5px;line-height:1.62;color:#3a4452}
  .copy p{margin-bottom:16px}
  .copy h2{font-size:22px;color:var(--orange);margin-bottom:14px}
  .repair__copy{top:60px}
  .repair__photo{bottom:0;height:330px;background:linear-gradient(135deg,var(--blue) 0%,#2c3b4c 45%,var(--gold) 80%,#d8d8d8 100%);clip-path:polygon(0 18%,100% 0,100% 100%,0 100%)}

  .tech__brand{position:absolute;top:70px;left:0;width:100%}
  .tech__title{position:absolute;top:150px;width:100%;text-align:center;font-size:22px;color:var(--gold)}
  .tech__steps{position:absolute;top:200px;left:28px;right:26px;list-style:none}
  .tech__steps li{display:flex;gap:14px;align-items:flex-start;margin-bottom:22px;font-size:14px;line-height:1.45}
  .tech__icon{flex:0 0 44px;height:44px;border-radius:50%;border:2px solid var(--gold);display:flex;align-items:center;justify-content:center}
  .tech__promise{position:absolute;top:690px;left:30px;right:30px;text-align:center;font-size:20px;line-height:1.3;color:var(--gold);font-weight:700}
  .tech__close{position:absolute;top:810px;left:34px;right:34px;text-align:center;font-size:14px;line-height:1.6;color:var(--blue-pale)}

  .emergency__copy{top:60px}
  .emergency__hours{position:absolute;top:620px;left:34px}
  .emergency__photo{bottom:0;height:330px;background:linear-gradient(180deg,#9cc07a 0%,#5d7f45 40%,var(--gold) 70%,#4d4d4d 100%);clip-path:polygon(0 18%,100% 0,100% 100%,0 100%)}
</style>
</head>
<body>

<!-- OUTSIDE SPREAD -->
<section class="sheet sheet--outside" aria-label="Brochure outside">

  <article class="panel services">
    <div class="photo services__photo" role="img" aria-label="Photo of a white service truck with company graphics parked by trees"></div>
    <div class="services__head">
      <h2 class="heading">Our Services</h2>
      <div class="hours">
        <svg width="34" height="34" viewBox="0 0 34 34" aria-hidden="true"><circle cx="17" cy="17" r="14" fill="none" stroke="var(--blue-deep)" stroke-width="3"/><path d="M17 9v8h7" fill="none" stroke="var(--blue-deep)" stroke-width="3" stroke-linecap="round"/></svg>
        <span class="hours__num">24</span>
      </div>
    </div>
    <ul class="services__list">
      <li>Mobile Hydraulic Repair</li>
      <li>We come to you</li>
      <li>Mobile Fleet Service and repairs at your yard or job site</li>
      <li>Complete Lube service, oil changes, fluid service and more at your yard or job site</li>
      <li>Roadside Assistance</li>
      <li>Advanced Computer Diagnostics</li>
    </ul>
    <h3 class="heading services__tag">We Come To You...</h3>
    <p class="services__copy">To minimize your equipment downtime and operating costs, Ironline Fleet Services brings the shop to your door so your crew can keep working while we handle the repair.</p>
    <div class="callbar">
      <span class="callbar__label">CALL US NOW</span>
      <span class="callbar__phone"><svg width="16" height="16" viewBox="0 0 24 24" aria-hidden="true"><path d="M6.6 10.8a15 15 0 0 0 6.6 6.6l2.2-2.2c.3-.3.7-.4 1-.2 1.1.4 2.3.6 3.6.6.6 0 1 .4 1 1V20c0 .6-.4 1-1 1A17 17 0 0 1 3 4c0-.6.4-1 1-1h3.5c.6 0 1 .4 1 1 0 1.3.2 2.5.6 3.6.1.3 0 .7-.2 1z" fill="var(--gold)"/></svg>1-888-555-0142</span>
    </div>
  </article>

  <article class="panel panel--blue contact">
    <div class="brand contact__brand"><span class="brand__mark"></span><span class="brand__name">Ironline Fleet</span></div>
    <p class="contact__dot">USDOT#2219840</p>
    <h3 class="heading contact__lead">We Come To You...</h3>
    <h2 class="heading contact__title">Mobile Fleet Service</h2>
    <div class="contact__bar">CALL US NOW <svg width="16" height="16" viewBox="0 0 24 24" aria-hidden="true"><path d="M6.6 10.8a15 15 0 0 0 6.6 6.6l2.2-2.2c.3-.3.7-.4 1-.2 1.1.4 2.3.6 3.6.6.6 0 1 .4 1 1V20c0 .6-.4 1-1 1A17 17 0 0 1 3 4c0-.6.4-1 1-1h3.5c.6 0 1 .4 1 1 0 1.3.2 2.5.6 3.6.1.3 0 .7-.2 1z" fill="var(--blue-deep)"/></svg> 1-888-555-0142</div>
    <address class="contact__lines">
      dana@ironlinerentals.com<br>
      www.ironlinerentals.com<br><br>
      4120 Cedar Mill Road<br>
      Lake Harlow, FL 33500
    </address>
    <div class="photo contact__photo" role="img" aria-label="Photo of a yellow compact skid steer loader"></div>
  </article>

  <article class="panel cover">
    <div class="brand cover__brand"><span class="brand__mark"></span><span class="brand__name">Ironline Fleet</span></div>
    <div class="photo cover__photo" role="img" aria-label="Photo of yellow excavators on a dirt job site under a blue sky"></div>
    <div class="hours cover__hours">
      <svg width="46" height="46" viewBox="0 0 34 34" aria-hidden="true"><circle cx="17" cy="17" r="14" fill="none" stroke="var(--blue-deep)" stroke-width="3"/><path d="M17 9v8h7" fill="none" stroke="var(--blue-deep)" stroke-width="3" stroke-linecap="round"/></svg>
      <div><div class="hours__num">24</div><div class="hours__label">HOURS</div></div>
    </div>
    <h1 class="heading cover__title">Mobile Fleet Service</h1>
    <div class="callbar">
      <span class="callbar__label">CALL US NOW</span>
      <span class="callbar__phone"><svg width="16" height="16" viewBox="0 0 24 24" aria-hidden="true"><path d="M6.6 10.8a15 15 0 0 0 6.6 6.6l2.2-2.2c.3-.3.7-.4 1-.2 1.1.4 2.3.6 3.6.6.6 0 1 .4 1 1V20c0 .6-.4 1-1 1A17 17 0 0 1 3 4c0-.6.4-1 1-1h3.5c.6 0 1 .4 1 1 0 1.3.2 2.5.6 3.6.1.3 0 .7-.2 1z" fill="var(--gold)"/></svg>1-888-555-0142</span>
    </div>
  </article>
</section>

<!-- INSIDE SPREAD -->
<section class="sheet sheet--inside" aria-label="Brochure inside">

  <article class="panel repair">
    <div class="copy repair__copy">
      <h2 class="heading">Mobile Hydraulic Repair</h2>
      <p>Mobile Hose Repair Service, 24/7, 365 Days, specializing in reducing customers' equipment downtime and operating cost, by coming to you with a fully stocked truck and a mobile workshop.</p>
      <p>Ironline Mobile Hydraulic Repair provides the fastest hydraulic hose replacement and industrial hose repair service in the area. Our on-site hydraulic repair is available 24/7, and is a simple solution that minimizes equipment downtime and eliminates the need for our customers to leave their job site or facility to locate a new hose.</p>
      <p>Our trucks are fully loaded with fittings and hoses to fit and make new hoses on demand exactly as the customer needs. We do it all on site and save you time from running around looking for a replacement hose.</p>
    </div>
    <div class="photo repair__photo" role="img" aria-label="Photo of a technician working on hydraulic equipment"></div>
  </article>

  <article class="panel panel--blue tech">
    <div class="brand tech__brand"><span class="brand__mark"></span><span class="brand__name">Ironline Fleet</span></div>
    <h2 class="heading tech__title">The Service Technician Will:</h2>
    <ol class="tech__steps">
      <li><span class="tech__icon"><svg width="20" height="20" viewBox="0 0 24 24" aria-hidden="true"><path d="M4 12l5 5L20 6" fill="none" stroke="var(--gold)" stroke-width="3" stroke-linecap="round"/></svg></span><span>Quickly assess the situation and failure.</span></li>
      <li><span class="tech__icon"><svg width="20" height="20" viewBox="0 0 24 24" aria-hidden="true"><path d="M4 12l5 5L20 6" fill="none" stroke="var(--gold)" stroke-width="3" stroke-linecap="round"/></svg></span><span>We will remove the failed hose to use it as a template to make a new one.</span></li>
      <li><span class="tech__icon"><svg width="20" height="20" viewBox="0 0 24 24" aria-hidden="true"><path d="M4 12l5 5L20 6" fill="none" stroke="var(--gold)" stroke-width="3" stroke-linecap="round"/></svg></span><span>The truck is fully equipped to be able to custom fabricate a replacement hose to match exactly what you need.</span></li>
      <li><span class="tech__icon"><svg width="20" height="20" viewBox="0 0 24 24" aria-hidden="true"><path d="M4 12l5 5L20 6" fill="none" stroke="var(--gold)" stroke-width="3" stroke-linecap="round"/></svg></span><span>We will then install the custom made hydraulic hose assembly on site without the need of having to move or transport the machine.</span></li>
      <li><span class="tech__icon"><svg width="20" height="20" viewBox="0 0 24 24" aria-hidden="true"><path d="M4 12l5 5L20 6" fill="none" stroke="var(--gold)" stroke-width="3" stroke-linecap="round"/></svg></span><span>We will then work with the customer to ensure the equipment is up and running before leaving the jobsite.</span></li>
    </ol>
    <p class="heading tech__promise">Our hydraulic hose repair service trucks are available day and night to fulfill your needs.</p>
    <p class="tech__close">To minimize your equipment downtime and operating costs, Ironline Fleet Services strives to be your go-to call for on-location hydraulic hose replacement.</p>
  </article>

  <article class="panel emergency">
    <div class="copy emergency__copy">
      <h2 class="heading">Emergency Hydraulic Assistance:</h2>
      <p>Between our different locations we have several fully equipped and stocked service trucks to meet your needs on the road. We offer onsite hydraulic repair &amp; diagnostics whether it's during regular operating hours, after hours, weekends, or holidays.</p>
      <p>We understand that your business depends on your trucks being on the road and meeting your promised delivery schedule.</p>
      <p>Whether it's at your shop, jobsite, or on the road, we are there to serve. We carry many of the common parts and items needed on the roadside.</p>
    </div>
    <div class="hours emergency__hours">
      <svg width="46" height="46" viewBox="0 0 34 34" aria-hidden="true"><circle cx="17" cy="17" r="14" fill="none" stroke="var(--blue-deep)" stroke-width="3"/><path d="M17 9v8h7" fill="none" stroke="var(--blue-deep)" stroke-width="3" stroke-linecap="round"/></svg>
      <div><div class="hours__num">24</div><div class="hours__label">HOURS</div></div>
    </div>
    <div class="photo emergency__photo" role="img" aria-label="Photo of a yellow skid steer loaded on a trailer beside a service truck"></div>
  </article>
</section>

</body>
</html>
```